Flyer design for carpet cleaning

We want to design a flyer for our new wing of business. Carpet and upholstery cleaning. We want it to match with the previous branding so please refer out website. Www.brivelcora.co.uk and see the carpet section. We currently have 4 services
Carpet and rug (cleaning and stain protection coating)
Upholstery and curtain (cleaning and stain protection coating)
Floor and patio (cleaning and polishing)
Antimicrobial (90 days self disinfecting coating)
Our price list is on the website I will attach some qr codes that I would like to put on the website.
Please use these terms
- quickest dry time
-24 hours call out
-based in London
-100% satisfaction guaranteed
-Low moisture cleaning
-Nano technology based stain protectant
- long lasting antimicrobial protection
Adding photos or not adding is designer choice and even putting price list or not is designer choice. The prices can be starting from format or full price list at the back page and other details in front

```html
<!DOCTYPE html>
<html lang="en">
<head>
<meta charset="utf-8">
<title>Brivelcora – Carpet &amp; Upholstery Cleaning Flyer</title>
<link href="https://fonts.googleapis.com/css2?family=Montserrat:wght@400;500;600;700;800&display=swap" rel="stylesheet">
<style>
  :root {
    --backdrop: #5f6062;
    --paper: #ffffff;
    --sky: #70cff3;
    --brand-blue: #1b9ad6;
    --deep-blue: #1f5fae;
    --navy: #1f3552;
    --ink: #1b1b1b;
    --muted: #333333;
    --photo-light: #d9d4cb;
    --photo-dark: #8d8a84;
  }
  * { margin: 0; padding: 0; box-sizing: border-box; }
  html, body {
    width: 1200px; height: 800px; overflow: hidden;
    background: var(--backdrop);
    font-family: "Montserrat", Arial, sans-serif;
  }
  .flyer {
    position: absolute; left: 332px; top: 20px;
    width: 536px; height: 760px;
    background: var(--paper); overflow: hidden;
  }
  .shapes { position: absolute; inset: 0; }
  .brand {
    position: absolute; left: 22px; top: 72px; width: 130px;
    text-align: center; font-size: 20px; font-weight: 700; color: var(--brand-blue);
  }
  .headline {
    position: absolute; left: 20px; top: 142px;
    font-size: 46px; font-weight: 800; line-height: 0.99; color: var(--ink);
    letter-spacing: -0.5px;
  }
  .headline .first { font-weight: 600; }
  .kicker { position: absolute; left: 23px; top: 307px; font-size: 11px; font-weight: 500; color: var(--ink); }
  .kicker b { font-weight: 700; }
  .promise { position: absolute; left: 23px; top: 326px; font-size: 12.4px; font-weight: 600; color: var(--brand-blue); }
  .section-title {
    position: absolute; font-size: 18px; font-weight: 700; color: var(--navy);
    padding-bottom: 3px; border-bottom: 2.5px solid var(--brand-blue);
  }
  .services-title { left: 23px; top: 378px; }
  .features-title { left: 285px; top: 367px; }
  .service { position: absolute; left: 23px; display: flex; align-items: center; gap: 9px; }
  .service-icon {
    width: 35px; height: 35px; border-radius: 50%; background: var(--navy);
    display: flex; align-items: center; justify-content: center; flex-shrink: 0;
  }
  .service-name { font-size: 9.8px; font-weight: 700; color: var(--ink); }
  .service-note { font-size: 9.6px; font-weight: 400; color: var(--muted); margin-top: 1px; }
  .features { position: absolute; left: 286px; top: 406px; list-style: none; }
  .features::before {
    content: ""; position: absolute; left: 6.5px; top: 8px; width: 3px; height: 200px; background: var(--navy);
  }
  .feature {
    position: relative; padding-left: 29px; font-size: 15.4px; font-weight: 500; color: var(--ink);
    line-height: 18px; margin-bottom: 9.5px;
  }
  .feature::before {
    content: ""; position: absolute; left: 0; top: 1px; width: 16px; height: 16px;
    border-radius: 50%; border: 3.5px solid var(--navy); background: #fff;
  }
  .cta-label { position: absolute; left: 22px; top: 665px; font-size: 22px; font-weight: 700; color: #fff; letter-spacing: 0.3px; }
  .phone { position: absolute; left: 21px; top: 709px; display: flex; align-items: center; gap: 10px;
    font-size: 25px; font-weight: 800; color: var(--navy); letter-spacing: 0.5px; }
  .contacts { position: absolute; left: 324px; top: 702px; color: #fff; font-size: 12px; font-weight: 500; }
  .contact { display: flex; align-items: center; gap: 7px; margin-bottom: 6px; }
</style>
</head>
<body>
<main class="flyer">
  <svg class="shapes" width="536" height="760" viewBox="0 0 536 760">
    <defs>
      <linearGradient id="photoTone" x1="0" y1="0" x2="1" y2="1">
        <stop offset="0" stop-color="var(--photo-light)"/>
        <stop offset="0.6" stop-color="#b8b3aa"/>
        <stop offset="1" stop-color="var(--photo-dark)"/>
      </linearGradient>
    </defs>
    <path class="hero-photo" role="img" aria-label="Photo of a technician in a white protective suit spraying antimicrobial coating in a bright city apartment lounge"
      d="M230 0 L536 0 L536 331 L320 331 Q295 331 282 308 L192 160 Q178 136 186 108 Z"
      fill="url(#photoTone)"/>
    <path d="M230 0 L186 108 Q178 136 192 160 L282 308 Q295 331 320 331 L536 331"
      fill="none" stroke="var(--deep-blue)" stroke-width="3"/>
    <path class="headline-panel" d="M0 138 L170 138 Q178 138 182 145 L268 282 Q273 291 262 291 L0 291 Z" fill="var(--sky)"/>
    <path class="cta-band" d="M0 662 L242 662 Q249 662 254 668 L276 695 L0 695 Z" fill="var(--navy)"/>
    <path class="contact-stripe" d="M247 667 Q256 662 262 670 L333 760 L318 760 Z" fill="var(--deep-blue)"/>
    <path class="contact-band" d="M284 695 L536 695 L536 760 L334 760 Z" fill="var(--brand-blue)"/>
  </svg>

  <header class="brand">Brivelcora</header>

  <h1 class="headline"><span class="first">Best</span><br>reliable<br>service.</h1>

  <p class="kicker">ANTIMICROBIAL COATING - <b>BRIVELCORA</b></p>
  <p class="promise">Longlasting shield for up to 90 days!</p>

  <h2 class="section-title services-title">OUR SERVICES:</h2>

  <div class="service" style="top:419px">
    <span class="service-icon"><svg width="20" height="20" viewBox="0 0 20 20" fill="none" stroke="#fff" stroke-width="1.3"><rect x="3" y="3" width="14" height="14"/><rect x="6" y="6" width="8" height="8"/></svg></span>
    <div><div class="service-name">Carpet and Rug</div><div class="service-note">(cleaning and stain protection coating)</div></div>
  </div>
  <div class="service" style="top:470px">
    <span class="service-icon"><svg width="20" height="20" viewBox="0 0 20 20" fill="none" stroke="#fff" stroke-width="1.3"><rect x="5" y="5" width="10" height="6" rx="1.5"/><rect x="2" y="9" width="16" height="5" rx="2"/><path d="M4 14v2M16 14v2"/></svg></span>
    <div><div class="service-name">Upholstery and Curtain</div><div class="service-note">(cleaning and stain protection coating)</div></div>
  </div>
  <div class="service" style="top:522px">
    <span class="service-icon"><svg width="20" height="20" viewBox="0 0 20 20" fill="none" stroke="#fff" stroke-width="1.2"><rect x="3" y="3" width="14" height="14"/><path d="M3 10L10 3M3 17L17 3M10 17L17 10M3 10L10 17M3 3L17 17M10 3L17 10"/></svg></span>
    <div><div class="service-name">Floor and Patio</div><div class="service-note">(cleaning and polishing)</div></div>
  </div>
  <div class="service" style="top:574px">
    <span class="service-icon"><svg width="22" height="22" viewBox="0 0 22 22" fill="none" stroke="#fff" stroke-width="1.2"><circle cx="11" cy="11" r="9"/><circle cx="11" cy="11" r="4"/><path d="M5 5L17 17"/></svg></span>
    <div><div class="service-name">Antimicrobial</div><div class="service-note">(90 days self disinfecting coating)</div></div>
  </div>

  <h2 class="section-title features-title">OUR SPECIAL FEATURES:</h2>
  <ul class="features">
    <li class="feature">Quickest dry time</li>
    <li class="feature">24 hours call out</li>
    <li class="feature">Based in London</li>
    <li class="feature">Low moisture cleaning</li>
    <li class="feature">100% satisfaction<br>guaranteed</li>
    <li class="feature">Nano technology<br>based stain protectant</li>
    <li class="feature">long lasting<br>antimicrobial protection</li>
  </ul>

  <p class="cta-label">CALL US NOW</p>
  <p class="phone">
    <svg width="24" height="24" viewBox="0 0 24 24" fill="var(--navy)"><path d="M6.6 10.8a15 15 0 0 0 6.6 6.6l2.2-2.2c.3-.3.7-.4 1-.2 1.1.4 2.3.6 3.6.6.6 0 1 .4 1 1V20c0 .6-.4 1-1 1A17 17 0 0 1 3 4c0-.6.4-1 1-1h3.5c.6 0 1 .4 1 1 0 1.3.2 2.5.6 3.6.1.3 0 .7-.2 1z"/></svg>
    02079461873
  </p>

  <div class="contacts">
    <div class="contact"><svg width="13" height="13" viewBox="0 0 14 14" fill="none" stroke="#fff" stroke-width="1.1"><circle cx="7" cy="7" r="6"/><ellipse cx="7" cy="7" rx="2.6" ry="6"/><path d="M1 7h12"/></svg>www.brivelcora.co.uk</div>
    <div class="contact"><svg width="13" height="13" viewBox="0 0 14 14" fill="none" stroke="#fff" stroke-width="1.1"><rect x="1" y="3" width="12" height="8"/><path d="M1 3l6 5 6-5"/></svg>info@brivelcora.co.uk</div>
  </div>
</main>
</body>
</html>
```